TRELBY Construction Group business card for distribution

A business card detailing our services, with our phone number and email address.
- Groundworks / Foundations / Drainage
- Landscaping / Hard Landscaping / Patios / Decking
- Fencing
The card should include company logo and be in the same colours.

Target Market(s)
Domestic Houses
Industry/Entity Type
Construction
Contact Information for Business Card
Phone Number - 07731 248 905 / 07612093184. Email address: trelbygroup@fenwickmail.com
Font styles to use
Serif
Sans Serif
Colors
F0912C
F2A743
F7CA91
FBE8D2
FDF5EE
Requirements
Must have
- Contact numbers. Photos of past work. Company Logo

Nice to have
- Company Logo

```html
<!DOCTYPE html>
<html lang="en">
<head>
<meta charset="utf-8">
<title>TRELBY Construction Group – Business Card</title>
<link href="https://fonts.googleapis.com/css2?family=Montserrat:wght@700&family=Lato:wght@400;700&display=swap" rel="stylesheet">
<style>
  :root {
    --ink: #231f20;
    --orange: #f0912c;
    --orange-soft: #f2a743;
    --paper: #ffffff;
    --backdrop: #ece8e3;
    --photo-sky: #8fa9c4;
    --photo-wall: #b9bcbd;
    --photo-road: #4a4c4e;
  }
  * { margin: 0; padding: 0; box-sizing: border-box; }
  html, body { width: 1200px; height: 900px; overflow: hidden; }
  body { background: var(--backdrop); position: relative; font-family: "Lato", sans-serif; }

  .card {
    position: absolute;
    left: 250px;
    width: 700px;
    height: 400px;
    background: var(--paper);
    box-shadow: 0 10px 28px rgba(0,0,0,.18);
    overflow: hidden;
  }
  .card--front { top: 40px; }
  .card--back  { top: 470px; }
  .card svg { position: absolute; inset: 0; width: 700px; height: 400px; }

  .brand {
    position: absolute;
    width: 250px;
    color: var(--paper);
    font-family: "Montserrat", sans-serif;
    font-weight: 700;
    line-height: 1;
    display: flex;
    align-items: center;
    gap: 14px;
    white-space: nowrap;
  }
  .brand__mark { width: 28px; height: 28px; background: var(--orange); flex: none; }
  .brand__name { display: flex; flex-direction: column; gap: 9px; }
  .brand__title { font-size: 44px; letter-spacing: 2px; }
  .brand__sub { font-size: 10.5px; letter-spacing: 1.4px; }
  .card--front .brand { left: 412px; top: 247px; }
  .card--back .brand { left: 404px; top: 34px; }

  .contact {
    position: absolute;
    left: 56px;
    top: 168px;
    color: var(--paper);
    list-style: none;
    font-size: 19px;
  }
  .contact li { display: flex; align-items: center; gap: 10px; margin-bottom: 6px; }
  .contact svg { position: static; width: 18px; height: 18px; flex: none; }

  .services { position: absolute; left: 56px; top: 262px; color: var(--paper); }
  .services__title { color: var(--orange); font-weight: 700; font-size: 24px; margin-bottom: 4px; }
  .services ul { list-style: none; font-size: 17px; line-height: 1.32; }
  .services li::before { content: "\2726"; color: var(--orange); font-size: 12px; margin-right: 8px; vertical-align: 2px; }
</style>
</head>
<body>

<section class="card card--front" aria-label="Card front">
  <svg viewBox="0 0 700 400">
    <defs>
      <linearGradient id="photoTone" x1="0" y1="0" x2="0.6" y2="1">
        <stop offset="0" stop-color="var(--photo-sky)"/>
        <stop offset="0.35" stop-color="var(--photo-wall)"/>
        <stop offset="1" stop-color="var(--photo-road)"/>
      </linearGradient>
    </defs>
    <polygon points="0,0 310,0 420,400 0,400" fill="url(#photoTone)" role="img" aria-label="Photo of completed groundworks: a tarmac service road with drainage channel beside a building"/>
    <polygon points="310,0 320,0 430,400 420,400" fill="var(--ink)"/>
    <polygon points="324,0 330,0 440,400 434,400" fill="var(--orange)"/>
    <polygon points="372,225 700,225 700,335 402,335" fill="var(--ink)"/>
  </svg>
  <div class="brand">
    <span class="brand__mark"></span>
    <span class="brand__name">
      <span class="brand__title">TRELBY</span>
      <span class="brand__sub">CONSTRUCTION GROUP LTD</span>
    </span>
  </div>
</section>

<section class="card card--back" aria-label="Card back">
  <svg viewBox="0 0 700 400">
    <polygon points="0,0 335,0 445,400 0,400" fill="var(--ink)"/>
    <polygon points="341,0 347,0 457,400 451,400" fill="var(--orange)"/>
    <polygon points="352,12 700,12 700,122 382,122" fill="var(--ink)"/>
  </svg>
  <div class="brand">
    <span class="brand__mark"></span>
    <span class="brand__name">
      <span class="brand__title">TRELBY</span>
      <span class="brand__sub">CONSTRUCTION GROUP LTD</span>
    </span>
  </div>

  <ul class="contact">
    <li>
      <svg viewBox="0 0 24 24"><path fill="var(--orange)" d="M6.6 10.8a15 15 0 0 0 6.6 6.6l2.2-2.2a1 1 0 0 1 1-.25 11.4 11.4 0 0 0 3.6.57 1 1 0 0 1 1 1V20a1 1 0 0 1-1 1A17 17 0 0 1 3 4a1 1 0 0 1 1-1h3.5a1 1 0 0 1 1 1c0 1.25.2 2.45.57 3.57a1 1 0 0 1-.25 1z"/></svg>
      <span>07731 248 905</span>
    </li>
    <li>
      <svg viewBox="0 0 24 24"><path fill="var(--orange)" d="M6.6 10.8a15 15 0 0 0 6.6 6.6l2.2-2.2a1 1 0 0 1 1-.25 11.4 11.4 0 0 0 3.6.57 1 1 0 0 1 1 1V20a1 1 0 0 1-1 1A17 17 0 0 1 3 4a1 1 0 0 1 1-1h3.5a1 1 0 0 1 1 1c0 1.25.2 2.45.57 3.57a1 1 0 0 1-.25 1z"/></svg>
      <span>07612093184</span>
    </li>
    <li>
      <svg viewBox="0 0 24 24"><rect x="2" y="5" width="20" height="14" fill="var(--orange)"/><path d="M2 5l10 8 10-8" fill="none" stroke="var(--ink)" stroke-width="1.6"/></svg>
      <span>trelbygroup@fenwickmail.com</span>
    </li>
  </ul>

  <div class="services">
    <h2 class="services__title">Our Services</h2>
    <ul>
      <li>Groundworks / Foundations</li>
      <li>Drainage / Landscaping</li>
      <li>Hard Landscaping / Patios</li>
      <li>Decking / Fencing</li>
    </ul>
  </div>
</section>

</body>
</html>
```